An animal window cleaning business card

I want a business card design that includes a logo and tells people I am a WINDOW WASHING COMPANY right away.
Were based in Maine, we do window cleaning, pressure washing, and gutter cleaning. We like Pine trees, the Ocean, state of Maine symbols, Lobsters, Moose, Huskies, etc. My business name is "BRIGHT PANE WINDOWS"
The card could also be designed to look like a gift credit card with a 50$ value.

Target Market(s)

my target audience is older folks with disposable money who live on the ocean or have secondary homes for vacation in Maine

Industry/Entity Type

Cleaning Services

Contact Information for Business Card

2.5x3" plastic if possible.

Font styles to use
Sans Serif

Requirements
Must have
• a symbol, or a logo that tells people I am a window washing company Instantly.
The words BRIGHT PANE, my phone number, my name, MY email
Nice to have
• a lobster holding a squeegee, or a stylized cartoonish version of a human huskie holding a squeegee,
Should not have
• a lighthouse
small hard to read text

```html
<!DOCTYPE html>
<html lang="en">
<head>
<meta charset="utf-8">
<title>Bright Pane Windows – Business Card</title>
<link rel="stylesheet" href="https://fonts.googleapis.com/css2?family=Jost:wght@500;800&family=Oswald:wght@600&family=Kaushan+Script&family=Lato:ital,wght@0,700;1,400&display=swap">
<style>
  :root {
    --page-bg: #e7e5e1;
    --card-light: #f4f6f8;
    --card-mist: #dfe6ee;
    --card-warm: #eadfd2;
    --title-blue: #1d5ea8;
    --wave-blue: #135aa0;
    --wave-deep: #0b3f7a;
    --wave-edge: #8a6f55;
    --badge-blue: #134d8f;
    --badge-deep: #0a3466;
    --gold: #d6c8a6;
    --gold-soft: #cbc1aa;
    --white: #ffffff;
    --figure-dark: #2a2a2e;
    --figure-mid: #4a4a52;
  }
  * { margin: 0; padding: 0; box-sizing: border-box; }
  html, body {
    width: 1200px;
    height: 969px;
    overflow: hidden;
    background: var(--page-bg);
  }
  .business-card {
    position: absolute;
    left: 80px;
    top: 187px;
    width: 1040px;
    height: 594px;
    overflow: hidden;
    background: linear-gradient(135deg, var(--card-mist) 0%, var(--card-light) 45%, var(--card-warm) 100%);
    box-shadow: 0 10px 30px rgba(0,0,0,0.18);
  }
  .card-art {
    position: absolute;
    inset: 0;
    width: 1040px;
    height: 594px;
    z-index: 0;
  }
  .brand-name,
  .gift-value,
  .contact { z-index: 1; }
  .brand-name {
    position: absolute;
    left: 278px;
    top: 66px;
    color: var(--title-blue);
    font-family: "Jost", sans-serif;
    line-height: 1;
  }
  .brand-name .line-top {
    display: block;
    font-weight: 500;
    font-size: 62px;
    letter-spacing: 0.5px;
  }
  .brand-name .line-bottom {
    display: block;
    font-weight: 800;
    font-size: 80px;
    margin-top: 2px;
  }
  .gift-value {
    position: absolute;
    left: 742px;
    top: 135px;
    width: 240px;
    text-align: center;
    color: var(--white);
    font-family: "Oswald", sans-serif;
    font-weight: 600;
    font-size: 104px;
    line-height: 1;
  }
  .contact {
    position: absolute;
    right: 48px;
    text-align: right;
    line-height: 1;
  }
  .contact-name {
    top: 378px;
    font-family: "Kaushan Script", cursive;
    font-size: 60px;
    color: var(--gold);
  }
  .contact-phone {
    top: 470px;
    font-family: "Lato", sans-serif;
    font-weight: 700;
    font-size: 48px;
    color: var(--gold);
    letter-spacing: 1px;
  }
  .contact-email {
    top: 530px;
    font-family: "Lato", sans-serif;
    font-style: italic;
    font-weight: 400;
    font-size: 24px;
    color: var(--gold-soft);
  }
</style>
</head>
<body>
  <div class="business-card">
    <svg class="card-art" viewBox="0 0 1040 594" xmlns="http://www.w3.org/2000/svg">
      <defs>
        <linearGradient id="waveFill" x1="0" y1="0" x2="1" y2="1">
          <stop offset="0" stop-color="var(--wave-blue)"/>
          <stop offset="1" stop-color="var(--wave-deep)"/>
        </linearGradient>
        <radialGradient id="badgeFill" cx="0.5" cy="0.45" r="0.6">
          <stop offset="0" stop-color="var(--badge-blue)"/>
          <stop offset="1" stop-color="var(--badge-deep)"/>
        </radialGradient>
        <linearGradient id="figureFill" x1="0" y1="0" x2="0" y2="1">
          <stop offset="0" stop-color="var(--figure-mid)"/>
          <stop offset="1" stop-color="var(--figure-dark)"/>
        </linearGradient>
      </defs>

      <path class="wave-edge" d="M405,594 C540,515 640,415 740,235 C785,160 890,118 1040,110" fill="none" stroke="var(--wave-edge)" stroke-width="6"/>
      <path class="wave-band" d="M430,594 C560,520 660,420 760,240 C805,168 905,128 1040,123 L1040,594 Z" fill="url(#waveFill)"/>

      <path class="cleaner-figure" role="img" aria-label="Silhouette of a window cleaner raising a squeegee"
            d="M30,100 L250,100 Q262,100 262,112 L262,232 L422,232 Q434,232 434,244 L434,594 L10,594 L10,120 Q10,100 30,100 Z"
            fill="url(#figureFill)" opacity="0.9"/>

      <g class="value-badge" transform="translate(862 195)" fill="url(#badgeFill)">
        <rect x="-86" y="-86" width="172" height="172"/>
        <rect x="-86" y="-86" width="172" height="172" transform="rotate(15)"/>
        <rect x="-86" y="-86" width="172" height="172" transform="rotate(30)"/>
        <rect x="-86" y="-86" width="172" height="172" transform="rotate(45)"/>
        <rect x="-86" y="-86" width="172" height="172" transform="rotate(60)"/>
        <rect x="-86" y="-86" width="172" height="172" transform="rotate(75)"/>
      </g>
    </svg>

    <h1 class="brand-name">
      <span class="line-top">BRIGHT PANE</span>
      <span class="line-bottom">WINDOWS</span>
    </h1>

    <div class="gift-value">50$</div>

    <p class="contact contact-name">Daniel Harper</p>
    <p class="contact contact-phone">207-555-0148</p>
    <p class="contact contact-email">info@brightpanewindows.com</p>
  </div>
</body>
</html>
```